Stationary Set and Logo Update **PAYMENT GUARANTEED**

Stationery Design and Logo Update

About Us

Trindex Supply is a wholesale distributor of OEM [original brand] and compatible [generic brand] parts and supplies for use in copiers, faxes, printers, and multi-function machines. In plain English…we sell all the parts and supplies [such as toner] that make up any office equipment which outputs an image on paper.

Trindex was the 1st distributor to develop and sell a generic brand copier part in the United States. We have been in business since 1972 [nearly 40 years]. Our tagline is "The Steady Choice," as in our company was the first alternative product that copier dealers had to buying original brand copier parts. Trindex is known for offering reliable and cost-effective OEM and compatible products.

Project

We require a fresh, modern and corporate identity. Please submit a stationary package inclusive of a double-sided business card (2" x 3.5"), letterhead (8.5'x11"), and standard #10 envelope (4-1/8” x 9-1/2). You may use our current logo or preferably your take on an updated one. If an attempt is made in updating the logo #004D8E or a similar hue should be used as the primary color.

The design should be clean, simple, modern and professional and make an immediate impact.

Target Market(s)

Copier and printer dealers who lease and service imaging equipment in the United States and Latin America.

Industry/Entity Type

Business

Requirements
Must have
• Simple, clean, modern and professional. Please use #004D8E or a similar hue as the primary color. Letterhead must accommate (2) addresses. We have 2 locations.
Nice to have
• A simple, modern update to our current logo. https://assets.mailvorbo.example/fs030/5520384417702/img/418.jpg
Should not have
• More than (2) colors on logo.

```html
<!DOCTYPE html>
<html lang="en">
<head>
<meta charset="utf-8">
<title>Trindex Stationery Concept</title>
<link href="https://fonts.googleapis.com/css2?family=Open+Sans:ital,wght@0,400;0,600;0,700;1,400;1,700&display=swap" rel="stylesheet">
<style>
:root{
  --bg:#d3d4d6;
  --paper:#ffffff;
  --brand:#0d4a8f;
  --brand-light:#2a62a3;
  --ink-grey:#8c8f94;
  --ink-dark:#3b3d40;
  --rule:#b8b6dc;
  --pattern-tint:rgba(184,182,220,.22);
  --crop:#8a8b8e;
  --label:#ffffff;
}
*{margin:0;padding:0;box-sizing:border-box}
html,body{width:1200px;height:900px;overflow:hidden}
body{background:var(--bg);font-family:"Open Sans",Arial,sans-serif;position:relative;color:var(--ink-dark)}
.section-label{position:absolute;color:var(--label);font-size:10.5px;font-weight:700;font-style:italic}
.set-title{position:absolute;right:28px;top:108px;color:var(--label);font-size:10.5px}
.set-title b{font-weight:700;font-style:italic}
.crops{position:absolute;left:0;top:0;width:1200px;height:900px}
.crops line{stroke:var(--crop);stroke-width:0.8}

.sheet{position:absolute;background:var(--paper);box-shadow:2px 3px 6px rgba(0,0,0,.35);overflow:hidden}
.pattern{position:absolute}

.logo{position:absolute;display:flex;align-items:center;gap:3px}
.logo-dot{width:9px;height:9px;border-radius:50%;background:var(--brand)}
.logo-name{font-size:17px;font-weight:700;color:var(--brand);line-height:1;letter-spacing:-.3px}
.tagline{position:absolute;text-align:right;font-weight:700;color:var(--ink-grey);font-size:6.5px;line-height:7px;text-transform:uppercase}
.tagline small{display:block;font-size:5px;text-transform:none;font-weight:600}

/* letterhead */
.letterhead{left:43px;top:127px;width:499px;height:645px;border-radius:12px}
.lh-pattern-top{left:0;top:38px;width:499px;height:90px;background:linear-gradient(180deg,transparent 0%,var(--pattern-tint) 45%,transparent 100%)}
.lh-pattern-right{right:0;top:160px;width:60px;height:110px;background:linear-gradient(90deg,transparent,var(--pattern-tint))}
.lh-pattern-left{left:0;top:490px;width:60px;height:120px;background:linear-gradient(270deg,transparent,var(--pattern-tint))}
.lh-address{position:absolute;top:15px;font-size:5.6px;line-height:8.2px;color:var(--ink-grey)}
.lh-address strong{font-weight:700}
.lh-writing-area{position:absolute;left:45px;top:106px;width:409px;height:494px;border-radius:10px;background:linear-gradient(180deg,#ffffff 0%,#f5f5f6 60%,#e7e7e9 100%);border:1px solid #e2e2e4}
.lh-directory{position:absolute;left:30px;right:20px;top:617px;display:flex;justify-content:space-between}
.lh-dept{text-align:center;font-size:6px}
.lh-dept strong{display:block;color:var(--brand);font-weight:700;border-bottom:.6px solid var(--rule);padding-bottom:2px;margin-bottom:2px}
.lh-dept span{color:var(--ink-grey);font-style:italic}

/* business card */
.card{width:208px;height:117px;border-radius:10px}
.card-front{left:632px;top:155px}
.card-back{left:632px;top:355px;background:var(--brand)}
.card-front .pattern{left:0;top:15px;width:208px;height:60px;background:linear-gradient(180deg,transparent 0%,var(--pattern-tint) 50%,transparent 100%)}
.card-back .pattern{left:0;top:35px;width:208px;height:60px;background:linear-gradient(180deg,transparent 0%,var(--brand-light) 55%,transparent 100%)}
.card-name{position:absolute;right:14px;top:10px;text-align:right;font-size:9.5px;font-weight:600;color:var(--brand)}
.card-name em{display:block;font-size:6.5px;font-weight:400;color:var(--ink-grey);border-bottom:.6px solid var(--rule);padding-bottom:1px}
.card-contact{position:absolute;left:114px;top:39px;font-size:6.3px;line-height:9.6px;color:var(--brand);list-style:none}
.card-contact li{display:flex;align-items:center;gap:4px}
.card-contact b{font-weight:700}
.card-contact i{font-style:italic}
.card-contact svg{width:7px;height:7px;fill:none;stroke:var(--brand);stroke-width:1.1}
.card-offices{position:absolute;left:14px;top:48px;font-size:4.6px;line-height:5.8px;color:var(--ink-dark)}
.card-offices strong{color:var(--brand);font-weight:700}
.card-offices p{margin-bottom:4px}
.card-back .logo-dot{background:#fff;width:11px;height:11px}
.card-back .logo-name{color:#fff;font-size:22px}
.card-back .tagline{color:#fff;text-align:left;font-size:6.3px;line-height:7px}

/* envelope */
.envelope{left:615px;top:520px;width:557px;height:242px}
.env-pattern{left:0;top:0;width:557px;height:242px;background:linear-gradient(160deg,var(--pattern-tint) 0%,transparent 30%,transparent 45%,var(--pattern-tint) 70%,transparent 100%)}
.env-address{position:absolute;left:33px;top:207px;font-size:5.6px;line-height:7.5px;color:var(--brand);font-weight:700;border-bottom:.6px solid var(--rule);padding-bottom:2px;width:190px}
</style>
</head>
<body>

<div class="section-label" style="left:75px;top:98px">Letterhead</div>
<div class="section-label" style="left:647px;top:120px">Business card</div>
<div class="section-label" style="left:1059px;top:496px">Envelope</div>
<div class="set-title"><b>Trindex</b> | Stationary Design Concept | <b>W.I.P.</b></div>

<svg class="crops" viewBox="0 0 1200 900" aria-hidden="true">
  <line x1="43" y1="104" x2="43" y2="118"/><line x1="542" y1="104" x2="542" y2="118"/>
  <line x1="20" y1="127" x2="34" y2="127"/><line x1="550" y1="127" x2="564" y2="127"/>
  <line x1="20" y1="772" x2="34" y2="772"/><line x1="550" y1="772" x2="564" y2="772"/>
  <line x1="43" y1="780" x2="43" y2="794"/><line x1="542" y1="780" x2="542" y2="794"/>
  <line x1="632" y1="135" x2="632" y2="148"/><line x1="840" y1="135" x2="840" y2="148"/>
  <line x1="612" y1="155" x2="625" y2="155"/><line x1="847" y1="155" x2="860" y2="155"/>
  <line x1="612" y1="272" x2="625" y2="272"/><line x1="847" y1="272" x2="860" y2="272"/>
  <line x1="632" y1="280" x2="632" y2="293"/><line x1="840" y1="280" x2="840" y2="293"/>
  <line x1="632" y1="335" x2="632" y2="348"/><line x1="840" y1="335" x2="840" y2="348"/>
  <line x1="612" y1="355" x2="625" y2="355"/><line x1="847" y1="355" x2="860" y2="355"/>
  <line x1="612" y1="472" x2="625" y2="472"/><line x1="847" y1="472" x2="860" y2="472"/>
  <line x1="632" y1="480" x2="632" y2="493"/><line x1="840" y1="480" x2="840" y2="493"/>
</svg>

<section class="sheet letterhead">
  <div class="pattern lh-pattern-top" role="img" aria-label="Flowing line pattern"></div>
  <div class="pattern lh-pattern-right" role="img" aria-label="Flowing line pattern"></div>
  <div class="pattern lh-pattern-left" role="img" aria-label="Flowing line pattern"></div>
  <div class="lh-address" style="left:31px">
    <strong>Corporate Office</strong><br>
    2290 Northeast 12th Street Coral Springs, FL 33065<br>
    Toll Free: 800.555.0140 Local: 954.555.0172 Fax: 954.555.0188
  </div>
  <div class="lh-address" style="left:226px">
    <strong>Trindex West</strong><br>
    Sierra Gate Commerce Park #4 1720 Alder Way Reno, NV 89502<br>
    Toll Free: 800.555.0166 Fax: 775.555.0149
  </div>
  <div class="logo" style="right:14px;top:16px"><span class="logo-dot"></span><span class="logo-name">Trindex</span></div>
  <div class="tagline" style="right:14px;top:35px">The Steady<br>Choice<small>since 1972</small></div>
  <div class="lh-writing-area"></div>
  <div class="lh-directory">
    <div class="lh-dept"><strong>General Info</strong><span>info@trindex.com</span></div>
    <div class="lh-dept"><strong>Sales or Customer Relations</strong><span>lmarsh@trindex.com</span></div>
    <div class="lh-dept"><strong>International Sales</strong><span>rolvera@trindex.com</span></div>
    <div class="lh-dept"><strong>Purchasing</strong><span>dkemp@trindex.com</span></div>
    <div class="lh-dept"><strong>Research &amp; Development</strong><span>tom.breslin@trindex.com</span></div>
  </div>
</section>

<section class="sheet card card-front">
  <div class="pattern" role="img" aria-label="Flowing line pattern"></div>
  <div class="card-name">Marla Ventosa<em>Marketing Director</em></div>
  <ul class="card-contact">
    <li><svg viewBox="0 0 8 8"><path d="M2 1 L3 3 L2.5 4 Q3.5 5.5 4.5 5.8 L5.5 5 L7 6.5 L6 7.5 Q2 7 0.8 2 Z"/></svg><span><b>Toll Free:</b> <i>800.555.0140</i></span></li>
    <li><svg viewBox="0 0 8 8"></svg><span><b>Direct:</b> <i>954.555.0121</i></span></li>
    <li><svg viewBox="0 0 8 8"><rect x=".6" y="1.5" width="6.8" height="5"/><path d="M.6 1.5 L4 4.5 L7.4 1.5"/></svg><i>mventosa@trindex.com</i></li>
    <li><svg viewBox="0 0 8 8"><circle cx="4" cy="4" r="3.2"/><path d="M.8 4 H7.2"/></svg><i>www.trindex.com</i></li>
  </ul>
  <div class="card-offices">
    <p><strong>Corporate Office</strong><br>2290 NE 12th Street<br>Coral Springs, FL 33065</p>
    <p><strong>Trindex West</strong><br>West Coast Fulfillment Center<br>Sierra Gate Commerce Park #4<br>1720 Alder Way<br>Reno, NV 89502</p>
  </div>
</section>

<section class="sheet card card-back">
  <div class="pattern" role="img" aria-label="Flowing line pattern"></div>
  <div class="logo" style="left:98px;top:34px"><span class="logo-dot"></span><span class="logo-name">Trindex</span></div>
  <div class="tagline" style="left:10px;top:80px">The Steady<br>Choice<small style="padding-left:30px">since 1972</small></div>
</section>

<section class="sheet envelope">
  <div class="pattern env-pattern" role="img" aria-label="Flowing line pattern"></div>
  <div class="logo" style="right:10px;top:12px"><span class="logo-dot"></span><span class="logo-name">Trindex</span></div>
  <div class="tagline" style="right:10px;top:31px">The Steady<br>Choice<small>since 1972</small></div>
  <div class="env-address">Corporate Office<br>2290 Northeast 12th Street Coral Springs, FL 33065</div>
</section>

</body>
</html>
```